We are looking to design a black on white bourbon label for a new brand
in att we have added
1. the bottle we need to use (wine bottle in black)
2. some industry examples (Look at horse rider label good example of where we need to go)
3. horses and cowboys illistrations

The brand will be Called BRASSMOOR RIDGE. we want an old school feeling label prohibition style.

What we need on the label is
1. visual = Bucking Horse + rider cowboy + lasso forming a circle
2. Name = Brassmoor Ridge Bourbon Straight Aged Whiskey
3. Product info = 70 CL 40 ABV
4. Distilled in the Wild Wild West WWW.BRASSMOORRIDGEWHISKEY.EXAMPLE

```html
<!DOCTYPE html>
<html lang="en">
<head>
<meta charset="utf-8">
<title>Brassmoor Ridge Whiskey Label</title>
<link rel="stylesheet" href="https://fonts.googleapis.com/css2?family=Germania+One&family=Michroma&family=Rye&display=swap">
<style>
  :root {
    --canvas: #ffffff;
    --paper: #f1efea;
    --ink: #3a3a3a;
    --ink-deep: #1c1c1c;
  }
  html, body {
    margin: 0;
    padding: 0;
    width: 972px;
    height: 1200px;
    overflow: hidden;
    background: var(--canvas);
  }
  .label-canvas {
    position: relative;
    width: 972px;
    height: 1200px;
  }
  .label {
    position: absolute;
    left: 166px;
    top: 40px;
    width: 640px;
    height: 1120px;
  }
  .frame-outer { fill: var(--paper); stroke: var(--ink); stroke-width: 4; }
  .frame-band { fill: var(--ink); }
  .frame-gap { fill: var(--paper); }
  .frame-inner { fill: var(--paper); stroke: var(--ink); stroke-width: 3; }
  .ribbon { fill: var(--paper); stroke: var(--ink); stroke-width: 3; }
  .ribbon-fold { fill: none; stroke: var(--ink); stroke-width: 2; }
  .brand-name {
    font-family: "Rye", serif;
    font-size: 24px;
    fill: var(--ink-deep);
    letter-spacing: 1px;
  }
  .product-title {
    font-family: "Germania One", serif;
    font-size: 108px;
    fill: var(--ink);
    letter-spacing: 1px;
  }
  .edition-line {
    font-family: "Michroma", sans-serif;
    font-size: 34px;
    fill: var(--ink);
  }
  .product-info {
    font-family: "Rye", serif;
    font-size: 14px;
    fill: var(--ink);
  }
</style>
</head>
<body>
<main class="label-canvas">
  <svg class="label" viewBox="0 0 640 1120" xmlns="http://www.w3.org/2000/svg">
    <defs>
      <path id="label-shape" d="M 40 140 H 80 V 100 H 200 Q 320 0 440 100 H 560 V 140 H 600 V 420 Q 640 560 600 700 V 980 H 560 V 1020 H 440 Q 320 1120 200 1020 H 80 V 980 H 40 V 700 Q 0 560 40 420 Z"/>
      <path id="ribbon-arc" d="M 110 262 Q 320 214 530 262"/>
      <radialGradient id="scene-tone" cx="50%" cy="50%" r="55%">
        <stop offset="0%" stop-color="#2a2a2a"/>
        <stop offset="60%" stop-color="#8c8c8c"/>
        <stop offset="100%" stop-color="#f1efea"/>
      </radialGradient>
    </defs>

    <use href="#label-shape" class="frame-outer"/>
    <use href="#label-shape" class="frame-band" transform="translate(320 560) scale(0.955) translate(-320 -560)"/>
    <use href="#label-shape" class="frame-gap" transform="translate(320 560) scale(0.925) translate(-320 -560)"/>
    <use href="#label-shape" class="frame-inner" transform="translate(320 560) scale(0.9) translate(-320 -560)"/>

    <rect class="crest" x="300" y="112" width="40" height="60" rx="6" fill="#6a6a6a" role="img" aria-label="Small bottle crest ornament"/>

    <path class="ribbon" d="M 82 278 L 104 250 Q 320 196 536 250 L 558 278 L 540 290 Q 320 240 100 290 Z"/>
    <path class="ribbon-fold" d="M 112 252 Q 320 202 528 252"/>
    <text class="brand-name" text-anchor="middle">
      <textPath href="#ribbon-arc" startOffset="50%">BRASSMOOR RIDGE</textPath>
    </text>

    <rect class="hero-illustration" x="110" y="305" width="420" height="390" rx="30" fill="url(#scene-tone)" role="img" aria-label="Bucking horse with cowboy rider swinging a lasso that forms a circle"/>

    <g class="title-block" transform="rotate(-13 320 820)">
      <text class="product-title" x="320" y="800" text-anchor="middle">WHISKEY</text>
      <text class="edition-line" x="345" y="842" text-anchor="middle">LIMITED</text>
      <text class="edition-line" x="335" y="880" text-anchor="middle">EDITION</text>
      <text class="product-info" x="335" y="904" text-anchor="middle">70 CL 40 ABV</text>
    </g>
  </svg>
</main>
</body>
</html>
```